Business card design needed

A business card and logo for my energy healing practice Tarrawin's Healing Spring. It should match my website www.tarrawinshealingspring-example.com in colours and atmosphere. It should look at bit rustic in combination with nature linking in with the natural healing techniques I offer in a heritage country town in NSW Australia. My business also includes a directory of other health and healing practitioners 'The Spring'. It would be nice if a graphic impression of the attached picture of the water feature in my front yard can be used.

Industry/Entity Type

Health

Contact Information for Business Card

Tarrawin's Healing Spring, Delphine Ashcroft, 14 Larchfield St, Wattleford NSW 2688, M. 0491 363 718, info@tarrawinshealingspring-example.com, www.tarrawinshealingspring-example.com,
Energy Healing - Your Natural Heritage
Kinnectly/Murmurs see Capital Renewal

```html
<!DOCTYPE html>
<html lang="en">
<head>
<meta charset="utf-8">
<title>Delphine Ashcroft – Business Card</title>
<link href="https://fonts.googleapis.com/css2?family=Quicksand:wght@300;400;700&display=swap" rel="stylesheet">
<style>
  :root {
    --teal-deep: #2a625e;
    --teal-mid: #3f7f79;
    --teal-light: #80b6ae;
    --ink: #ffffff;
    --ink-soft: rgba(255, 255, 255, 0.9);
    --rule: rgba(255, 255, 255, 0.85);
  }
  html, body {
    margin: 0;
    padding: 0;
    width: 1200px;
    height: 705px;
    overflow: hidden;
  }
  .card {
    position: relative;
    width: 1200px;
    height: 705px;
    overflow: hidden;
    font-family: "Quicksand", sans-serif;
    color: var(--ink);
    background:
      radial-gradient(ellipse 70% 60% at 10% 100%, rgba(160, 210, 200, 0.55), transparent 70%),
      radial-gradient(ellipse 60% 50% at 85% 10%, rgba(30, 80, 76, 0.5), transparent 70%),
      linear-gradient(170deg, var(--teal-deep) 0%, var(--teal-mid) 45%, var(--teal-light) 100%);
  }
  .card-line {
    position: absolute;
    left: 0;
    width: 100%;
    margin: 0;
    text-align: center;
    white-space: nowrap;
    line-height: 1;
  }
  .holder-name {
    top: 76px;
    font-weight: 700;
    font-size: 76px;
    letter-spacing: 2px;
  }
  .address {
    top: 174px;
    font-weight: 300;
    font-size: 38px;
    color: var(--ink-soft);
  }
  .phone {
    top: 310px;
    font-weight: 300;
    font-size: 54px;
  }
  .email {
    top: 381px;
    font-weight: 300;
    font-size: 44px;
  }
  .website {
    top: 444px;
    font-weight: 300;
    font-size: 44px;
  }
  .tagline {
    top: 594px;
    font-weight: 400;
    font-size: 32px;
    color: var(--ink-soft);
  }
  .social {
    top: 635px;
    font-weight: 400;
    font-size: 32px;
    color: var(--ink-soft);
  }
  .divider {
    position: absolute;
    left: 90px;
    width: 1021px;
    height: 4px;
  }
  .divider-top { top: 252px; }
  .divider-bottom { top: 552px; }
</style>
</head>
<body>
  <div class="card">
    <h1 class="card-line holder-name">Delphine Ashcroft</h1>
    <p class="card-line address">14 Larchfield St, Wattleford NSW 2688</p>

    <svg class="divider divider-top" viewBox="0 0 1021 4" aria-hidden="true">
      <line x1="0" y1="2" x2="1021" y2="2" stroke="var(--rule)" stroke-width="2" stroke-dasharray="6 4"/>
    </svg>

    <p class="card-line phone">M. 0491 363 718</p>
    <p class="card-line email">info@tarrawinshealingspring-example.com</p>
    <p class="card-line website">www.tarrawinshealingspring-example.com</p>

    <svg class="divider divider-bottom" viewBox="0 0 1021 4" aria-hidden="true">
      <line x1="0" y1="2" x2="1021" y2="2" stroke="var(--rule)" stroke-width="2" stroke-dasharray="6 4"/>
    </svg>

    <p class="card-line tagline">Energy Healing - Your Natural Heritage</p>
    <p class="card-line social">Kinnectly/Murmurs see Capital Renewal</p>
  </div>
</body>
</html>
```